Mosquito and outdoor pest management

The uploaded logo must be integrated as the main theme of the card. I would like it to be modern and eye catching. Maybe some backround images or light silver metallic background.
Space enough at the base for contact info to be put in- phone numbers,emails,names,website.
Space on the back for short blog and lines for hand writing..calling card.
Target Market(s)
Commercial- golf courses, schools, outdoor function properties, pre event treatments.
Residential- retirement villages, townhome complexes and general houses
Industry/Entity Type
Management

```html
<!DOCTYPE html>
<html lang="en">
<head>
<meta charset="utf-8">
<title>Bayline Mosquito – Business Card</title>
<link rel="stylesheet" href="https://fonts.googleapis.com/css2?family=Open+Sans:wght@400;600;700&display=swap">
<style>
  :root {
    --page-bg: #e4e5e6;
    --card-bg: #f7f8f8;
    --card-edge: #c9cbcc;
    --brand-red: #c8262b;
    --ink: #262626;
    --faint-mark: rgba(200, 204, 206, 0.55);
  }
  * { margin: 0; padding: 0; box-sizing: border-box; }
  html, body {
    width: 1200px;
    height: 970px;
    overflow: hidden;
    background: var(--page-bg);
    font-family: "Open Sans", Arial, sans-serif;
  }
  .canvas {
    position: relative;
    width: 1200px;
    height: 970px;
  }
  .business-card {
    position: absolute;
    left: 120px;
    top: 218px;
    width: 960px;
    height: 534px;
    background: var(--card-bg);
    border: 1.5px solid var(--card-edge);
    border-radius: 26px;
    overflow: hidden;
    color: var(--ink);
  }
  .brand-mark-area {
    position: absolute;
    left: 520px;
    top: 150px;
    width: 380px;
    height: 380px;
    border-radius: 50%;
    background: radial-gradient(circle, var(--faint-mark) 0%, rgba(220,222,224,0) 70%);
  }
  .brand {
    position: absolute;
    left: 395px;
    top: 70px;
    display: flex;
    align-items: center;
    gap: 16px;
  }
  .brand-dot {
    width: 22px;
    height: 22px;
    border-radius: 50%;
    background: var(--brand-red);
  }
  .brand-name {
    font-size: 46px;
    font-weight: 700;
    color: var(--brand-red);
    letter-spacing: 0.5px;
    line-height: 1;
  }
  .person {
    position: absolute;
    left: 48px;
    top: 208px;
  }
  .person-name {
    font-size: 29px;
    font-weight: 700;
    color: var(--brand-red);
    line-height: 1.2;
  }
  .person-role {
    font-size: 22px;
    font-weight: 400;
    line-height: 1.3;
  }
  .contact-list {
    position: absolute;
    left: 48px;
    top: 298px;
    list-style: none;
    font-size: 22px;
    line-height: 32px;
  }
  .contact-list li {
    display: flex;
    align-items: center;
    gap: 10px;
  }
  .contact-icon {
    width: 18px;
    height: 18px;
    fill: var(--brand-red);
    flex: none;
  }
  .address {
    position: absolute;
    left: 48px;
    top: 440px;
    font-style: normal;
    font-size: 22px;
    line-height: 30px;
  }
</style>
</head>
<body>
<div class="canvas">
  <section class="business-card">
    <div class="brand-mark-area" role="img" aria-label="Faint enlarged brand mark decoration"></div>

    <div class="brand">
      <span class="brand-dot"></span>
      <span class="brand-name">Bayline Mosquito</span>
    </div>

    <div class="person">
      <p class="person-name">Daniel Hartfield</p>
      <p class="person-role">Director of operations</p>
    </div>

    <ul class="contact-list">
      <li>
        <svg class="contact-icon" viewBox="0 0 18 18" aria-hidden="true"><rect x="4" y="1" width="10" height="16" rx="2"/><rect x="6" y="3" width="6" height="8" fill="#f7f8f8"/></svg>
        <span>+ 000 000 0000</span>
      </li>
      <li>
        <svg class="contact-icon" viewBox="0 0 18 18" aria-hidden="true"><path d="M1 7c0-3 4-4 8-4s8 1 8 4v2h-4V7H5v2H1z"/><rect x="3" y="10" width="12" height="6" rx="1.5"/></svg>
        <span>+ 000 000 0000</span>
      </li>
      <li>
        <svg class="contact-icon" viewBox="0 0 18 18" aria-hidden="true"><rect x="1" y="4" width="16" height="11" rx="1"/><path d="M1.5 4.5 9 10l7.5-5.5" fill="none" stroke="#f7f8f8" stroke-width="1.5"/></svg>
        <span>info@baylinemosquito.com</span>
      </li>
      <li>
        <svg class="contact-icon" viewBox="0 0 18 18" aria-hidden="true"><circle cx="9" cy="9" r="8"/><path d="M1 9h16M9 1c-3 3-3 13 0 16M9 1c3 3 3 13 0 16" fill="none" stroke="#f7f8f8" stroke-width="1.2"/></svg>
        <span>www.baylinemosquito.com</span>
      </li>
    </ul>

    <address class="address">
      Level 4, 18 Harbour Lane<br>
      Marlow, 20, New South
    </address>
  </section>
</div>
</body>
</html>
```